Facebook & Instagram Design for: A Lantern for Pim - Notes of a Calm Hound

Need a Facebook Page and Instagram Page too for helping launch a book as a brand new author with a book on my old dog Pim and the Zen lessons he taught me.
Its all for folks who love dogs and especially rescue dog stories
Its all for folks who are interested in something slightly spiritual and for self growth
I attach the review copy from my publishers who are standing up a website but recommend a Facebook Page that is attached to my own personal one and an Instagram Page
I intend on publishing weekly "Pimsayings" (The dog was called Pim)
I intend on posting Zen talks (in lay man's terms)
I have a second book being written to follow on the one
Myself as an Author needs profiling
The book needs ALOT of promotion - and we can't travel!
I need to host a bunch of "book talks/launches"
Need to send folks to my website to by the book: Hard/Paperback/Kindle - which comes with book trailer
I have hundreds of photos to give
I have alot of sketches of the dog to share which did not make it into the book
My competition are books like:
Tobin & Us
A Cat Naps Beside Old Farmers
Talo
Duke Ferran's Setter
Lost Shepherd Road
Need this ASAP - publishing date is moved up to October 2021!
Link t Author hot Drop Box: https://www.fileharbor-vault.net/s/kq7wm2201935t4/XXRtplmNvQwerty3ab_KLop?v=0
Link to Dog Photos:
https://www.fileharbor-vault.net/s/pl3rt88vnaw02k/ZZT4k7mnop_Yrw2QLxwbcd9v?v=0
Updates
Hello, I will be in hospitaal having surgery on my neck and request tow more days to =make any kind of small changes. Thank you Harriet
Target Market(s)
Dog owners around the world, especially those wth rescue dogs and those looking for personal growth and those interested in Zen Buddhism
Industry/Entity Type
Author promoting soon to be published book/s
Requirements
Must have
- Author Photo/E-Mail Sign Up/Link to Instagram (see brief to design this)/Link to upcoming website/Link to Author Central (might need to design me something)/Photo Gallery
Nice to have
- Author features and Dog Images (I have new dogs we can show)
Should not have
- Cute - its a meaningful book

```html
<!DOCTYPE html>
<html lang="en">
<head>
<meta charset="utf-8">
<title>A Lantern for Pim – Notes of a Calm Hound</title>
<link rel="stylesheet" href="https://fonts.googleapis.com/css2?family=Merriweather:wght@700;900&family=Archivo+Black&family=Dancing+Script:wght@600&family=Oswald:wght@600&display=swap">
<style>
  :root {
    --bamboo-dark: #2f5a16;
    --bamboo-mid: #5f8d2a;
    --bamboo-light: #a9c25a;
    --headline: #ffffff;
    --tagline: #ffd21a;
    --button-blue: #1d3f8f;
    --button-edge: #ffffff;
    --ring-gold: #f2c21b;
    --portrait-bg: #3a3a3c;
    --stone-light: rgba(190,188,180,.95);
    --stone-dark: rgba(120,118,110,.85);
    --cover-top: #1f3c9e;
    --cover-mid: #3f7fd8;
    --cover-light: #b9dcf2;
    --cover-script: #7fd6ef;
    --cover-white: #ffffff;
  }
  * { box-sizing: border-box; margin: 0; padding: 0; }
  html, body { width: 1200px; height: 444px; overflow: hidden; background: #ffffff; }

  .banner {
    position: relative;
    width: 1200px;
    height: 444px;
    overflow: hidden;
    font-family: "Merriweather", Georgia, serif;
  }

  .bamboo-backdrop {
    position: absolute; inset: 0;
    background:
      linear-gradient(90deg, rgba(30,60,10,.35) 0%, rgba(30,60,10,0) 40%),
      linear-gradient(180deg, var(--bamboo-mid) 0%, var(--bamboo-light) 45%, var(--bamboo-mid) 75%, var(--bamboo-dark) 100%);
  }

  .stone-stack {
    position: absolute;
    left: 720px; top: -30px;
    width: 200px; height: 420px;
    background: radial-gradient(ellipse 50% 50% at 50% 50%, var(--stone-light) 0%, var(--stone-dark) 55%, rgba(120,118,110,0) 100%);
  }

  .headline {
    position: absolute;
    left: 42px; top: 18px;
    font-size: 48px;
    font-weight: 900;
    color: var(--headline);
    text-shadow: 0 2px 4px rgba(0,0,0,.45);
    white-space: nowrap;
  }

  .tagline {
    position: absolute;
    left: 44px; top: 94px;
    width: 700px;
    font-size: 26px;
    line-height: 33px;
    font-weight: 700;
    color: var(--tagline);
    text-shadow: 0 1px 3px rgba(0,0,0,.45);
  }

  .site-button {
    position: absolute;
    left: 40px; top: 185px;
    width: 232px; height: 46px;
    border: 2px solid var(--button-edge);
    border-radius: 12px;
    background: var(--button-blue);
    color: var(--headline);
    font-size: 20px;
    font-weight: 700;
    display: flex; align-items: center; justify-content: center;
    text-decoration: none;
  }

  .author-portrait {
    position: absolute;
    left: 568px; top: 152px;
    width: 288px; height: 288px;
    border-radius: 50%;
    border: 4px solid var(--ring-gold);
    background: radial-gradient(circle at 60% 45%, #6a6a6c 0%, var(--portrait-bg) 70%);
  }

  .book-cover {
    position: absolute;
    left: 912px; top: 7px;
    width: 256px; height: 424px;
    background: linear-gradient(180deg, var(--cover-top) 0%, var(--cover-mid) 42%, var(--cover-light) 55%);
    box-shadow: -6px 4px 12px rgba(0,0,0,.35);
    overflow: hidden;
    text-align: center;
  }
  .cover-photo {
    position: absolute;
    left: 0; top: 205px;
    width: 256px; height: 219px;
    background: linear-gradient(180deg, #9fc3a0 0%, #6f7c4a 45%, #4a4030 100%);
  }
  .cover-title {
    position: relative;
    margin-top: 34px;
    font-family: "Archivo Black", "Arial Black", sans-serif;
    color: var(--cover-white);
    line-height: 1;
  }
  .cover-title .lead { display: block; font-size: 27px; letter-spacing: .5px; }
  .cover-title .name { display: block; font-size: 52px; margin-top: 4px; }
  .cover-title .name small { font-size: 27px; margin-right: 4px; }
  .cover-subtitle {
    position: relative;
    margin-top: 12px;
    font-family: "Dancing Script", cursive;
    font-size: 24px;
    color: var(--cover-script);
  }
  .cover-stamp {
    position: absolute;
    left: 0; right: 0; top: 328px;
    font-family: "Oswald", sans-serif;
    font-size: 18px;
    line-height: 21px;
    color: var(--cover-script);
    letter-spacing: 1px;
  }
  .cover-author {
    position: absolute;
    left: 0; right: 0; bottom: 16px;
    font-family: "Oswald", sans-serif;
    font-size: 20px;
    color: var(--cover-white);
    letter-spacing: 1px;
  }
</style>
</head>
<body>
  <section class="banner">
    <div class="bamboo-backdrop" role="img" aria-label="Green bamboo stalks photo background"></div>
    <div class="stone-stack" role="img" aria-label="Balanced stack of grey zen stones"></div>

    <h1 class="headline">Notes of a Calm Hound</h1>
    <p class="tagline">for folks who love dogs and especially rescue dog stories</p>
    <a class="site-button" href="#">Visit Our Website</a>

    <div class="author-portrait" role="img" aria-label="Portrait of the author lying beside her brindle dog"></div>

    <div class="book-cover">
      <div class="cover-photo" role="img" aria-label="Brindle dog resting among pink flowers"></div>
      <div class="cover-title">
        <span class="lead">A LANTERN</span>
        <span class="name"><small>for</small>PIM</span>
      </div>
      <p class="cover-subtitle">Notes of a Calm Hound</p>
      <p class="cover-stamp">REVIEW<br>COPY</p>
      <p class="cover-author">HARRIET CALLOWAY</p>
    </div>
  </section>
</body>
</html>
```